New banner graphics for Velkora.com website

I've developed a software tool that helps businesses ensure they are working on their most valuable and important work.

I would like a banner graphic for my home page (www.velkora.com) that can somehow capture the value of focus and intentional outcomes.

I had an initial thought of a starry sky that shifts focus to a few bright stars, but while that might sound ok, I think my idea is lame hence I'm coming to you guys.

My sites two primary colors are a soft purple and gray.
#919EC1(purple)
#9E9E9E (gray)

Target Market(s)

B2B for enterprises. Typical customers are CFOs, CIOs/Heads of IT

Industry/Entity Type

Business Software

Number of Pages Required

1 page

Font styles to use
Sans Serif

Colors
b8a6cd
cedeed

Requirements
Must have
• I use Divi as my Wordpress theme and the current main landing page can be seen at www.velkora.com.
• My logo colors are:
• #919EC1(purple)
• #9E9E9E (gray)
Should not have
• Lots of distraction or visual "noise". I want to re-enforce the message that my software is focused on their business and not my products or website.

```html
<!DOCTYPE html>
<html lang="en">
<head>
<meta charset="utf-8">
<title>Velkora.com – Focused on your business</title>
<link href="https://fonts.googleapis.com/css2?family=Open+Sans:wght@300&family=Raleway:wght@200;300&display=swap" rel="stylesheet">
<style>
  :root {
    --brand-purple: #919ec1;
    --brand-gray: #9e9e9e;
    --ink: #2b2b2b;
    --slate: #4e5370;
    --accent-pink: #e0245e;
    --menu-slate: #4a5068;
    --rule: #1e1e1e;
    --lavender: #b8a6cd;
    --sky: #cedeed;
  }
  * { margin: 0; padding: 0; box-sizing: border-box; }
  html, body { width: 1200px; height: 1000px; overflow: hidden; background: #fff; }
  .page { position: relative; width: 1200px; height: 1000px; }

  .site-header { position: absolute; left: 0; top: 0; width: 1200px; height: 160px; }
  .brand-name {
    position: absolute; left: 103px; top: 58px;
    font-family: "Raleway", sans-serif; font-weight: 300;
    font-size: 52px; letter-spacing: 1px; color: var(--brand-gray);
  }
  .search-icon { position: absolute; left: 942px; top: 80px; }
  .menu-icon { position: absolute; left: 1037px; top: 84px; }
  .header-rule {
    position: absolute; left: 17px; top: 159px; width: 1162px; height: 2px; background: var(--rule);
  }

  .hero { position: absolute; left: 17px; top: 167px; width: 1163px; height: 419px; overflow: hidden; }
  .hero-photo {
    position: absolute; inset: 0;
    background:
      linear-gradient(180deg, rgba(245,240,250,0.5) 0%, rgba(0,0,0,0) 40%),
      linear-gradient(100deg, #d9cdb8 0%, #b89470 35%, #a27b58 55%, #d6c4d8 80%, #efe6f2 100%);
  }
  .hero-wash { position: absolute; inset: 0; }
  .hero-tagline {
    position: absolute; left: 21px; top: 175px;
    font-family: "Open Sans", sans-serif; font-weight: 300;
    font-size: 42px; line-height: 46px; color: #3a3a3a; letter-spacing: -0.5px;
  }
  .hero-tagline .highlight { color: var(--brand-purple); }

  .strategy-title {
    position: absolute; left: 0; top: 615px; width: 1200px; text-align: center;
    font-family: "Raleway", sans-serif; font-weight: 200;
    font-size: 104px; line-height: 98px; color: #111;
  }
  .strategy-subtitle {
    position: absolute; left: 0; top: 872px; width: 1200px; text-align: center;
    font-family: "Raleway", sans-serif; font-weight: 300;
    font-size: 50px; line-height: 48px; color: #333;
  }
  .strategy-subtitle .written { color: var(--slate); }
</style>
</head>
<body>
<div class="page">
  <header class="site-header">
    <div class="brand-name">velkora</div>
    <svg class="search-icon" width="34" height="34" viewBox="0 0 34 34" aria-label="Search">
      <circle cx="19" cy="14" r="10" fill="none" stroke="var(--accent-pink)" stroke-width="2.4"/>
      <line x1="12" y1="21" x2="4" y2="30" stroke="var(--accent-pink)" stroke-width="2.6" stroke-linecap="round"/>
    </svg>
    <svg class="menu-icon" width="34" height="26" viewBox="0 0 34 26" aria-label="Menu">
      <rect x="0" y="1" width="32" height="3" fill="var(--menu-slate)"/>
      <rect x="0" y="11" width="32" height="3" fill="var(--menu-slate)"/>
      <rect x="0" y="21" width="32" height="3" fill="var(--menu-slate)"/>
    </svg>
    <div class="header-rule"></div>
  </header>

  <section class="hero">
    <div class="hero-photo" role="img" aria-label="Photo of a person working on a laptop at a wooden desk with a coffee mug, notes and a pen"></div>
    <svg class="hero-wash" width="1163" height="419" viewBox="0 0 1163 419" aria-hidden="true">
      <defs>
        <linearGradient id="washLeft" x1="0" y1="0" x2="1" y2="0">
          <stop offset="0" stop-color="#cedeed" stop-opacity="0.95"/>
          <stop offset="0.4" stop-color="#dcd6ec" stop-opacity="0.85"/>
          <stop offset="0.75" stop-color="#b8a6cd" stop-opacity="0.2"/>
          <stop offset="1" stop-color="#b8a6cd" stop-opacity="0"/>
        </linearGradient>
      </defs>
      <path d="M0 0 H520 C420 120 420 300 380 419 H0 Z" fill="url(#washLeft)"/>
      <path d="M0 120 C300 150 600 260 1163 380" fill="none" stroke="#ffffff" stroke-opacity="0.5" stroke-width="40"/>
      <path d="M150 0 C500 40 800 200 1163 150" fill="none" stroke="#ffffff" stroke-opacity="0.25" stroke-width="60"/>
    </svg>
    <div class="hero-tagline">WE’RE FOCUSED<br>ON <span class="highlight">YOUR</span> BUSINESS.</div>
  </section>

  <h1 class="strategy-title">Is Your Business<br>Strategy</h1>
  <p class="strategy-subtitle"><span class="written">WRITTEN DOWN</span> or LOOSE THOUGHTS –<br>ON THE BEST OF DAYS.</p>
</div>
</body>
</html>
```